Magician | Speaker looks for an innovative business card design

I'm a magician and public speaker offering artistic and modern magical experiences.
I'm based in Brussels (Belgium.) I love magic performed up-close, creating a space of intimacy, even when I'm on stage.
The final design should communicate professionalism, elegance, artistry, and a friendly kind personality

I would like to see designs based either on my photos and/or the way I sign my name Theo Varn (see attached files for more info.)
Additional photos and more info about what I offer can be seen at www.theo-varn.net

My current business card design is also attached. I like the fact that the reverse of my current design includes quotes from master magicians about magic, changing the way my participants see the art of magic.

Note: I would like a double-sided card design. However, I need white space on the reverse to be able to write things on for my performances.

Details to include on the card:
Artist name: Theo Varn
Offer: magician + (public) speaker or magic + (public) speaking (the + sign can be replaced by another character, like a bullet or a pipe)
Phone: +32 471 236 519
Email: book@theo-varn.net
(optional) Website: www.theo-varn.net or theo-varn.net

Target Market(s)

Corporate, organisations, companies as well as individuals

Industry/Entity Type

Artists

Colors

Designer to choose colors to be used in the design.

Requirements
Nice to have
• A side with a mirror could be nice

```html
<!DOCTYPE html>
<html lang="en">
<head>
<meta charset="utf-8">
<title>Theo Varn – Business Card</title>
<link rel="stylesheet" href="https://fonts.googleapis.com/css2?family=Open+Sans:wght@400;600&display=swap">
<style>
  :root {
    --backdrop: #858585;
    --card-light: #e8e6e4;
    --brand-rose: #d64369;
    --text-on-rose: #ffffff;
    --photo-dark: #2a1a12;
    --photo-mid: #5b3a26;
    --photo-warm: #8a5a3a;
    --card-shadow: rgba(0, 0, 0, 0.35);
  }
  * { margin: 0; padding: 0; box-sizing: border-box; }
  html, body {
    width: 1200px;
    height: 900px;
    overflow: hidden;
    background: var(--backdrop);
    font-family: "Open Sans", Arial, sans-serif;
  }
  .card {
    position: absolute;
    top: 306px;
    width: 439px;
    height: 272px;
    border-radius: 10px;
    overflow: hidden;
    box-shadow: 1px 2px 4px var(--card-shadow);
  }
  .card--front { left: 150px; background: var(--card-light); }
  .card--back { left: 609px; }

  .front-wave { position: absolute; inset: 0; }

  .wordmark {
    position: absolute;
    left: 66px;
    top: 58px;
    font-size: 30px;
    font-weight: 400;
    color: var(--brand-rose);
    letter-spacing: 0.5px;
  }

  .identity {
    position: absolute;
    left: 24px;
    top: 205px;
    color: var(--text-on-rose);
  }
  .identity__name {
    font-size: 15px;
    font-weight: 600;
    letter-spacing: 0.3px;
    line-height: 18px;
  }
  .identity__role {
    font-size: 12px;
    line-height: 15px;
  }

  .contact {
    position: absolute;
    right: 24px;
    top: 197px;
    list-style: none;
    color: var(--text-on-rose);
    font-size: 12px;
    line-height: 16px;
    text-align: right;
  }
  .contact__item {
    display: flex;
    justify-content: flex-end;
    align-items: center;
    gap: 3px;
  }
  .contact__icon { width: 10px; height: 10px; fill: var(--text-on-rose); }

  .back-photo {
    width: 100%;
    height: 100%;
    background:
      radial-gradient(ellipse at 55% 30%, var(--photo-warm) 0%, transparent 55%),
      linear-gradient(180deg, var(--photo-mid) 0%, var(--photo-dark) 100%);
  }
</style>
</head>
<body>

<section class="card card--front" aria-label="Business card front">
  <svg class="front-wave" width="439" height="272" viewBox="0 0 439 272" aria-hidden="true">
    <path d="M0 156 C 80 138, 200 128, 300 136 C 370 141, 420 130, 439 92 L 439 272 L 0 272 Z"
          fill="var(--brand-rose)"/>
  </svg>

  <div class="wordmark">Theo Varn</div>

  <div class="identity">
    <p class="identity__name">THEO VARN</p>
    <p class="identity__role">Magician &amp; Public Speaker</p>
  </div>

  <ul class="contact">
    <li class="contact__item">+32 471 236 519
      <svg class="contact__icon" viewBox="0 0 10 10" aria-hidden="true">
        <path d="M2 0.5 L3.6 2.6 L2.7 3.8 C3.3 5 4.8 6.6 6.2 7.3 L7.4 6.4 L9.5 8 L8.4 9.5 C4.5 9.3 0.7 5.5 0.5 1.6 Z"/>
      </svg>
    </li>
    <li class="contact__item">book@theo-varn.net
      <svg class="contact__icon" viewBox="0 0 10 10" aria-hidden="true">
        <path d="M0.5 2 H9.5 V8.5 H0.5 Z M1.2 2.6 L5 5.6 L8.8 2.6" stroke="var(--brand-rose)" stroke-width="0.8"/>
      </svg>
    </li>
    <li class="contact__item">www.theo-varn.net
      <svg class="contact__icon" viewBox="0 0 10 10" aria-hidden="true">
        <circle cx="5" cy="5" r="4.5"/>
        <path d="M0.5 5 H9.5 M5 0.5 C3 3, 3 7, 5 9.5 M5 0.5 C7 3, 7 7, 5 9.5" stroke="var(--brand-rose)" stroke-width="0.7" fill="none"/>
      </svg>
    </li>
  </ul>
</section>

<section class="card card--back" aria-label="Business card back">
  <div class="back-photo" role="img"
       aria-label="Photograph of the magician performing a card trick at a wooden table for two smiling guests"></div>
</section>

</body>
</html>
```